Business card design needed

I need a business card design also to be used on fridge magnets. All the details above to be included on the card. I am a freelance book-keeper providing services to small to medium size business providing services in PLUV including training, consulting, BAS, IAS, preparation and lodgement, superannuation, workcover. I would like a design that is easy to read a see. Something that relates to the finance industry. A design that can be used for all other marketing products.

Target Market(s)

Small business mainly sole traders - trades people

Industry/Entity Type

Marketing

Contact Information for Business Card

Bramblewood Book-keeping Services Maren Vosk - PLUV Consultant BAS REGISTERED AGENT 27360519 PO Box 7316 Harrowmere North QLD 4127 0478152906

Logo Text

Bramblewood Book-keeping Services

Logo styles of interest
Emblem Logo
Pictorial/Combination Logo
Abstract Logo
Character Logo

```html
<!DOCTYPE html>
<html lang="en">
<head>
<meta charset="utf-8">
<title>Bramblewood Book-keeping Services – Business Card</title>
<link href="https://fonts.googleapis.com/css2?family=Source+Sans+3:wght@400;600&display=swap" rel="stylesheet">
<style>
  :root {
    --stage: #d9d9d9;
    --card: #ffffff;
    --ink: #4a4a4a;
    --blue: #3a9fd6;
    --green: #8cc63f;
    --dot-blue: #cfe1f1;
    --dot-green: #e4eed0;
    --dot-grey: #ececec;
  }
  html, body {
    margin: 0;
    width: 1200px;
    height: 900px;
    overflow: hidden;
    background: var(--stage);
    font-family: "Source Sans 3", "Myriad Pro", sans-serif;
  }
  .card {
    position: absolute;
    left: 120px;
    top: 183px;
    width: 960px;
    height: 534px;
    background: var(--card);
    box-shadow: 0 10px 30px rgba(0,0,0,0.25);
    overflow: hidden;
  }
  .card__edge {
    position: absolute;
    left: 0; right: 0; bottom: 0;
    height: 14px;
    background: var(--green);
  }
  .card__pattern {
    position: absolute;
    right: 0;
    top: 0;
    bottom: 14px;
    width: 560px;
    background:
      radial-gradient(ellipse at 65% 30%, var(--dot-blue) 0%, rgba(207,225,241,0) 50%),
      radial-gradient(ellipse at 85% 70%, var(--dot-green) 0%, rgba(228,238,208,0) 50%),
      linear-gradient(120deg, var(--dot-grey) 0%, var(--dot-grey) 55%, var(--dot-green) 100%);
    -webkit-mask-image: linear-gradient(to right, transparent 0%, #000 45%), linear-gradient(to bottom, #000 60%, transparent 100%);
    -webkit-mask-composite: source-in;
    mask-image: linear-gradient(to right, transparent 0%, #000 45%), linear-gradient(to bottom, #000 60%, transparent 100%);
    mask-composite: intersect;
  }
  .brand {
    position: absolute;
    left: 60px;
    top: 118px;
    display: flex;
    align-items: center;
    gap: 18px;
  }
  .brand__mark {
    width: 30px;
    height: 30px;
    border-radius: 50%;
    background: var(--blue);
  }
  .brand__name {
    margin: 0;
    font-weight: 400;
    font-size: 30px;
    line-height: 1.1;
    color: var(--green);
  }
  .person {
    position: absolute;
    left: 150px;
    top: 322px;
    color: var(--ink);
  }
  .person__name {
    margin: 0 0 6px;
    font-weight: 400;
    font-size: 44px;
    letter-spacing: 2px;
    color: var(--blue);
    text-transform: uppercase;
  }
  .person__role {
    margin: 0;
    font-size: 22px;
    line-height: 1.3;
  }
  .contact {
    position: absolute;
    left: 520px;
    top: 262px;
    color: var(--ink);
  }
  .contact__phone {
    margin: 0 0 6px;
    font-size: 38px;
    color: var(--blue);
  }
  .contact__phone-label {
    font-size: 22px;
    font-weight: 600;
    color: var(--ink);
    margin-right: 8px;
  }
  .contact__address {
    margin: 0;
    font-size: 21px;
    line-height: 1.25;
    font-style: normal;
  }
</style>
</head>
<body>
  <div class="card">
    <div class="card__pattern" role="img" aria-label="Decorative field of soft blue, green and grey circles"></div>

    <div class="brand">
      <span class="brand__mark"></span>
      <p class="brand__name">Bramblewood<br>Book-keeping Services</p>
    </div>

    <div class="person">
      <h1 class="person__name">Maren Vosk</h1>
      <p class="person__role">PLUV Consultant</p>
      <p class="person__role">BAS REGISTERED AGENT 27360519</p>
    </div>

    <div class="contact">
      <p class="contact__phone"><span class="contact__phone-label">PH:</span>0478152906</p>
      <address class="contact__address">PO Box 7316 Harrowmere North<br>QLD 4127</address>
    </div>

    <div class="card__edge"></div>
  </div>
</body>
</html>
```